Tavrinel House

I am looking at a A4 one sided fact sheet about the property I developed, which I can print off or send electronically
Our current logo is Navy blue and Maroon colors
House

```html
<!DOCTYPE html>
<html lang="en">
<head>
<meta charset="utf-8">
<title>Tavrinel House – Project Fact Sheet</title>
<link rel="stylesheet" href="https://fonts.googleapis.com/css2?family=Orbitron:wght@700&family=Mulish:wght@400;600&family=Open+Sans:wght@700&display=swap">
<style>
  :root {
    --navy: #1c2a5e;
    --maroon: #7f2428;
    --plum: #4a2a55;
    --row-blue: #c4e2f7;
    --ink: #1a1a1a;
    --white: #ffffff;
    --canvas: #f4f4f4;
  }
  * { box-sizing: border-box; margin: 0; padding: 0; }
  html, body { width: 924px; height: 1200px; overflow: hidden; }
  body { background: var(--canvas); font-family: "Mulish", sans-serif; color: var(--ink); position: relative; }

  .sheet { position: absolute; left: 80px; top: 102px; width: 772px; height: 998px; background: var(--white); overflow: hidden; }

  .masthead { position: absolute; left: 0; top: 0; width: 772px; height: 76px; background: var(--navy); }
  .masthead h1 { position: absolute; left: 68px; top: 14px; font-family: "Orbitron", sans-serif; font-weight: 700; font-size: 43px; letter-spacing: 1px; color: var(--white); }

  .brand { position: absolute; left: 64px; top: 90px; font-family: "Mulish", sans-serif; font-weight: 400; color: var(--navy); font-size: 20px; line-height: 21px; letter-spacing: 0.5px; }
  .office { position: absolute; left: 293px; top: 88px; color: var(--navy); font-size: 13.5px; line-height: 17.5px; }
  .contact { position: absolute; left: 445px; color: var(--navy); font-size: 14px; line-height: 15px; display: flex; align-items: flex-start; gap: 6px; }
  .contact.phone { top: 92px; font-weight: 600; font-size: 15px; }
  .contact.email { top: 121px; font-size: 13.5px; }
  .contact svg { flex: none; }

  .shapes { position: absolute; left: 0; top: 0; }

  .caption { position: absolute; left: 10px; top: 484px; width: 300px; color: var(--white); font-size: 13.5px; line-height: 17px; }

  .features { position: absolute; left: 0; top: 548px; width: 400px; }
  .features h2 { font-family: "Open Sans", sans-serif; font-weight: 700; font-size: 16.5px; color: var(--navy); margin-left: 16px; margin-bottom: 3px; }
  .feature-row { display: flex; font-size: 15px; line-height: 22.7px; padding-left: 16px; }
  .feature-row:nth-child(even) { background: linear-gradient(90deg, var(--row-blue) 70%, rgba(196,226,247,0) 100%); }
  .feature-row dt { width: 179px; flex: none; }
  .feature-row dd { flex: 1; }

  .strategy { position: absolute; left: 407px; top: 555px; width: 365px; height: 426px; background: var(--maroon); color: var(--white); padding: 18px 16px 0 25px; }
  .strategy h2 { font-family: "Open Sans", sans-serif; font-weight: 700; font-size: 16.5px; margin-bottom: 2px; }
  .strategy p { font-size: 13.6px; line-height: 20.2px; }
  .strategy p.closing { font-size: 13px; line-height: 20px; }
</style>
</head>
<body>
<main class="sheet">
  <header class="masthead"><h1>PROJECT FACT SHEET</h1></header>

  <div class="brand">HARBOURLINE<br>DEVELOPMENT<br>GROUP Pty Ltd</div>
  <address class="office" style="font-style:normal">Office Address<br>Level 1,<br>19 Marlow St,<br>Northport, QLD, 4100.</address>
  <div class="contact phone">
    <svg width="22" height="22" viewBox="0 0 22 22"><circle cx="11" cy="11" r="10" fill="none" stroke="var(--navy)" stroke-width="1.6"/><path d="M7.5 6 l2 0 l1 3 l-1.3 1 a6 6 0 0 0 3 3 l1-1.3 l3 1 l0 2 a1.5 1.5 0 0 1 -1.5 1.3 a9 9 0 0 1 -8.5 -8.5 a1.5 1.5 0 0 1 1.3 -1.5z" fill="var(--navy)"/></svg>
    <span>+61 0400 555 019</span>
  </div>
  <div class="contact email">
    <svg width="22" height="22" viewBox="0 0 22 22"><circle cx="11" cy="11" r="10" fill="none" stroke="var(--navy)" stroke-width="1.6"/><path d="M5 7 h12 v8 h-12z M5 7 l6 5 l6 -5" fill="none" stroke="var(--navy)" stroke-width="1.4"/></svg>
    <span>enquiries@harbourlinedev<br>.com.au</span>
  </div>

  <svg class="shapes" width="772" height="998" viewBox="0 0 772 998">
    <defs>
      <linearGradient id="tone-building" x1="0" y1="0" x2="0" y2="1">
        <stop offset="0" stop-color="#8fa8c8"/><stop offset="0.45" stop-color="#8a7f7a"/><stop offset="1" stop-color="#4e4a4a"/>
      </linearGradient>
      <linearGradient id="tone-gym" x1="0" y1="0" x2="1" y2="1">
        <stop offset="0" stop-color="#c9c4bb"/><stop offset="1" stop-color="#6e6a66"/>
      </linearGradient>
      <linearGradient id="tone-office" x1="0" y1="0" x2="0" y2="1">
        <stop offset="0" stop-color="#e8e6df"/><stop offset="0.6" stop-color="#a8b58a"/><stop offset="1" stop-color="#9a8f7f"/>
      </linearGradient>
      <linearGradient id="tone-city" x1="0" y1="0" x2="0" y2="1">
        <stop offset="0" stop-color="#9fa9a8"/><stop offset="0.5" stop-color="#7d8577"/><stop offset="1" stop-color="#a19787"/>
      </linearGradient>
    </defs>
    <polygon role="img" aria-label="Photograph of the finished Tavrinel House office building" points="0,163 557,163 330,523 0,523" fill="url(#tone-building)"/>
    <polygon points="0,476 350,476 320,523 0,523" fill="var(--maroon)"/>
    <polygon role="img" aria-label="Photograph of the building's staff gym" points="603,163 772,163 772,296 540,296" fill="url(#tone-gym)"/>
    <polygon role="img" aria-label="Photograph of the open-plan office and breakout area" points="578,323 772,323 772,523 442,523" fill="url(#tone-office)"/>
    <polygon role="img" aria-label="Aerial photograph of the city and river surrounding the site" points="0,831 355,831 255,981 0,981" fill="url(#tone-city)"/>
    <polygon points="280,983 375,983 327,890" fill="var(--plum)"/>
  </svg>

  <p class="caption">Photo of finished building 27-Calloway<br>-Rd-34</p>

  <section class="features">
    <h2>PROPERTY FEATURES</h2>
    <dl>
      <div class="feature-row"><dt>Name</dt><dd>Tavrinel House</dd></div>
      <div class="feature-row"><dt>Address</dt><dd>27 Calloway Road<br>Westbank</dd></div>
      <div class="feature-row"><dt>When Developed</dt><dd>2008</dd></div>
      <div class="feature-row"><dt>Value on Completion</dt><dd>$87m</dd></div>
      <div class="feature-row"><dt>Size</dt><dd>15,700m2 NLA</dd></div>
      <div class="feature-row"><dt>Type of Property</dt><dd>A Grade Commercial<br>Office Space</dd></div>
      <div class="feature-row"><dt>Quality rating</dt><dd>4 Star</dd></div>
      <div class="feature-row"><dt>Developed by</dt><dd>Harbourline Development<br>Group Pty Ltd</dd></div>
    </dl>
  </section>

  <section class="strategy">
    <h2>DEVELOPMENT STRATEGY</h2>
    <p>Tavrinel is a world class mining engineering firm. They had 6 offices spread out of a number of locations in the Southern part of Northport. Working with Tavrinel, we identified a site for their new headquarters. We purchased the land and applied for a development approval to develop a 15,700m2 office building on the site. We designed an office building around their requirements including their staff requirements, gym, bike rack, change rooms, outdoor dining areas, café, large car parking facility, storage etc.We appointed Crestmore Builders to undertake a “design and construct” contract to build the development. Construction lasted about 18 months and we completed an integrated fitout to get them into the office space quicker.</p>
    <p class="closing">The property was sold on completion to American based fund manager Valdris for $87.2m</p>
  </section>
</main>
</body>
</html>
```